BOLD & MINIMALIST DESIGN NEEDED

We want a very bold but minimalistic business card design that is impactful and utilizes both sides of the business card. Our current logo is included for your use.

We want bold fonts and good use of negative space. We don't want the logo to overpower the design.

Target Market(s)

Professionals who are building new commercial buildings.

Industry/Entity Type

Construction

Contact Information for Business Card

Name, Title, email, office phone, cell phone, website

Font styles to use
Serif
Sans Serif

Requirements
Must have
• Bold design!

```html
<!DOCTYPE html>
<html lang="en">
<head>
<meta charset="utf-8">
<title>Crestline Business Card</title>
<link rel="stylesheet" href="https://fonts.googleapis.com/css2?family=Open+Sans:wght@400;800&display=swap">
<style>
  :root {
    --backdrop: #88ff00;
    --card: #ffffff;
    --ink: #1a1a1a;
    --accent: #88ff00;
  }
  * { margin: 0; padding: 0; box-sizing: border-box; }
  html, body { width: 1200px; height: 504px; overflow: hidden; }
  body {
    background: var(--backdrop);
    font-family: "Open Sans", Arial, sans-serif;
    color: var(--ink);
    position: relative;
  }
  .card {
    position: absolute;
    top: 104px;
    width: 508px;
    height: 290px;
    background: var(--card);
  }
  .card--front { left: 65px; }
  .card--back { left: 600px; }

  .brand {
    position: absolute;
    display: flex;
    align-items: center;
    gap: 8px;
    font-weight: 800;
    color: var(--ink);
    letter-spacing: 0.02em;
    line-height: 1;
  }
  .brand__mark { background: var(--accent); flex: none; }
  .card--front .brand {
    left: 50%;
    top: 50%;
    transform: translate(-50%, -50%);
    font-size: 36px;
  }
  .card--front .brand__mark { width: 22px; height: 22px; }
  .card--back .brand {
    left: 74px;
    top: 193px;
    font-size: 15px;
    gap: 5px;
  }
  .card--back .brand__mark { width: 10px; height: 10px; }

  .identity { position: absolute; left: 65px; top: 60px; }
  .identity__name {
    font-size: 33px;
    font-weight: 400;
    line-height: 1;
    letter-spacing: 0.01em;
  }
  .identity__title {
    font-size: 12px;
    margin-top: 3px;
    margin-left: 3px;
    letter-spacing: 0.02em;
  }

  .contacts {
    position: absolute;
    right: 34px;
    top: 72px;
    list-style: none;
  }
  .contacts__item {
    display: flex;
    align-items: center;
    justify-content: flex-end;
    gap: 9px;
    height: 32px;
    margin-bottom: 10.5px;
    font-size: 14.5px;
  }
  .contacts__icon {
    width: 32px;
    height: 32px;
    border-radius: 50%;
    background: var(--accent);
    display: flex;
    align-items: center;
    justify-content: center;
  }
  .contacts__icon svg {
    width: 18px; height: 18px;
    fill: none; stroke: #fff; stroke-width: 1.3;
    stroke-linecap: round; stroke-linejoin: round;
  }
</style>
</head>
<body>
  <section class="card card--front">
    <div class="brand"><span class="brand__mark"></span>CRESTLINE</div>
  </section>

  <section class="card card--back">
    <div class="identity">
      <h1 class="identity__name">YOUR NAME</h1>
      <p class="identity__title">YOUR POSITION</p>
    </div>

    <div class="brand"><span class="brand__mark"></span>CRESTLINE</div>

    <ul class="contacts">
      <li class="contacts__item">yourmail@mailbox.com
        <span class="contacts__icon"><svg viewBox="0 0 18 18"><path d="M2 7 L9 2 L16 7 V16 H2 Z"/><path d="M2 7 L9 12 L16 7"/><path d="M2 16 L7 11 M16 16 L11 11"/></svg></span>
      </li>
      <li class="contacts__item">+000 0000 00000
        <span class="contacts__icon"><svg viewBox="0 0 18 18"><rect x="5" y="1.5" width="8" height="15" rx="1.5"/><path d="M5 4 H13 M5 14 H13"/></svg></span>
      </li>
      <li class="contacts__item">+9999 9999 99999
        <span class="contacts__icon"><svg viewBox="0 0 18 18"><path d="M4 2.5 L6.5 2.5 L7.5 6 L5.8 7.2 C6.8 9.3 8.7 11.2 10.8 12.2 L12 10.5 L15.5 11.5 V14 C15.5 15 14.7 15.5 14 15.5 C8 15.2 2.8 10 2.5 4 C2.5 3.3 3 2.5 4 2.5 Z"/><path d="M11 2.5 A4.5 4.5 0 0 1 15.5 7"/><path d="M11 5 A2 2 0 0 1 13 7"/></svg></span>
      </li>
      <li class="contacts__item">www.companyname.com
        <span class="contacts__icon"><svg viewBox="0 0 18 18"><circle cx="9" cy="9" r="7"/><ellipse cx="9" cy="9" rx="3" ry="7"/><path d="M2 9 H16 M3 5.5 H15 M3 12.5 H15"/></svg></span>
      </li>
    </ul>
  </section>
</body>
</html>
```